EILT: Landing Page - EXPRESS VERSAND
Zielgruppe
Es soll in kurzer Zeit (max 48 Stunden) eine kleine Ladingpage entstehen. Expressversand / Import von China nach Deutschland . Aufgrund der stark steigenden Luftfrachtraten aus China heraus hat sich unsere Firma Fracht-Kapazitäten gesichert. Diese sollen nun angeboten werden. Über eine Ladingpage sollen Anfragen generiert werden. Diese Anfragen werden dann mit einem Angebot von uns beantwortet. Expressversand / Import von China nach Deutschland
Aufgabenstellung
Die Seite soll beinhalten:
- 1-2 Bilder (z. B. Luftfracht, Logistik, Flugzeug, Cargo, etc)
- kurzer erklärender Text: z.B. 'jetzt Angebot anfordern und günstig aus China per Express versenden.' Inkl. Abholung, Verzollung und Zustellung. Kurze Laufzeit von nur 3-5 Tagen. ab 45€ / Paket
- Anfrage Formular, bestehend aus: , Abholadresse in China/Post Code, ZielAdresse Deutschland, Sendungsinformationen (wie viele Kartons, wie schwer ist ein Karton und welche Abmessungen L/B/H ), wann ist die Sendung in China abholbereit, optional: Sendungsinhalt (Ware, Zolltarifnummer/HS Code) , Firma, Name, email adresse
- optional ein Header/Laufband etc mit: Bis zum 19. Nov 21 versenden - Ware bis MegaSonntag erhalten!
- 24h Servicehotline, Tel: 0987/314265
- 2-3 Kundenreferenzen: Bilder von Personen mit Text : „Schneller Versand - nur 4 Tage Laufzeit“ , „1A Service, ohne Probleme“ , „gute Preise - nur zu empfehlen.“
Unser Firmenlogo kann - muss aber nicht auftauchen.
In der farblichen Gestaltung haben Sie freie Hand und freuen uns auf Ihre Vorschläge.
Aufgrund der Dringlichkeit sollte diese Landingpage innerhalb 48 Stunden 'live ' gehen.
WICHTIG: Die Page sollte von Ihnen auch veröffentlich werden. Aktuell nutzen wir den Kelvo Homepagebaukasten. Die Page kann aber auch durch andere Anbieter veröffentlicht werden , zb Pagerune

```html
<!DOCTYPE html>
<html lang="de">
<head>
<meta charset="utf-8">
<title>Velarix – Expressversand China nach Deutschland</title>
<link href="https://fonts.googleapis.com/css2?family=Fira+Sans:wght@300;400;500;600;700&display=swap" rel="stylesheet">
<style>
  :root {
    --blue: #0a80c0;
    --violet: #6a16f0;
    --orb: #3d20c6;
    --coral: #c94e3a;
    --ink: #151515;
    --field-line: #7a7a7a;
    --field-text: #222;
    --gold: #f6b40e;
    --white: #ffffff;
  }
  * { box-sizing: border-box; margin: 0; padding: 0; }
  html, body { width: 1200px; height: 1191px; overflow: hidden; }
  body {
    position: relative;
    background: var(--white);
    font-family: "Fira Sans", sans-serif;
    color: var(--ink);
  }
  .hero {
    position: absolute; left: 0; top: 0; width: 1200px; height: 494px;
    background: linear-gradient(115deg, var(--blue) 0%, #3b47d8 45%, var(--violet) 100%);
    clip-path: polygon(0 0, 100% 0, 100% 494px, 0 444px);
  }
  .hero__orb {
    position: absolute; left: 618px; top: 11px; width: 428px; height: 428px;
    border-radius: 50%; background: var(--orb);
  }
  .hero__visual {
    position: absolute; left: 512px; top: 82px; width: 609px; height: 308px;
    border-radius: 24px;
    background: linear-gradient(120deg, #2f6a78 0%, #e0b04a 45%, #c58f55 65%, #e9eaee 100%);
    opacity: .85;
  }
  .brand {
    position: absolute; left: 154px; top: 38px;
    display: flex; align-items: center; gap: 10px;
  }
  .brand__dot { width: 40px; height: 40px; border-radius: 50%; background: #e8628f; }
  .brand__name { font-size: 26px; font-weight: 700; color: var(--white); }
  .hero__title {
    position: absolute; left: 150px; top: 152px;
    font-size: 43px; line-height: 44px; font-weight: 700; color: var(--white);
    letter-spacing: -.3px;
  }
  .hotline__label {
    position: absolute; left: 153px; top: 348px; width: 276px; text-align: center;
    font-size: 19px; font-weight: 500; color: var(--white);
  }
  .hotline__pill {
    position: absolute; left: 153px; top: 378px; width: 276px; height: 46px;
    border-radius: 23px; background: var(--coral);
    display: flex; align-items: center; justify-content: center; gap: 10px;
    color: var(--white); font-size: 28px; font-weight: 700;
  }
  .intro {
    position: absolute; left: 0; top: 508px; width: 1200px; text-align: center;
    font-size: 21px; line-height: 32px; font-weight: 500; color: var(--ink);
  }
  .swirl { position: absolute; left: 124px; top: 496px; }
  .quote-form {
    position: absolute; left: 202px; top: 601px; width: 797px;
    display: grid; grid-template-columns: 249px 249px 249px; column-gap: 24px; row-gap: 17px;
  }
  .quote-form__field {
    height: 40px; border: 2px solid var(--field-line); border-radius: 4px;
    padding: 0 15px; display: flex; align-items: center;
    font-size: 13px; color: var(--field-text); background: var(--white);
  }
  .quote-form__send {
    position: absolute; left: 477px; top: 784px; width: 253px; height: 41px;
    border-radius: 21px; background: var(--coral); color: var(--white);
    display: flex; align-items: center; justify-content: center; gap: 10px;
    font-size: 17px; font-weight: 500;
  }
  .reviews {
    position: absolute; left: 0; top: 845px; width: 1200px; height: 346px;
    background: linear-gradient(100deg, var(--violet) 0%, #8f2ec4 45%, var(--coral) 100%);
    clip-path: polygon(0 49px, 100% 0, 100% 100%, 0 100%);
  }
  .reviews__mark {
    position: absolute; left: 148px; top: 892px;
    font-size: 130px; line-height: 1; font-weight: 700; color: #5416a8;
  }
  .reviews__title {
    position: absolute; left: 0; top: 916px; width: 1200px; text-align: center;
    font-size: 29px; font-weight: 500; color: var(--white);
  }
  .review-list {
    position: absolute; left: 153px; top: 985px;
    display: flex; gap: 14px;
  }
  .review {
    position: relative; width: 289px; height: 126px;
    background: rgba(70, 20, 120, .28);
  }
  .review__text {
    margin-top: 17px; text-align: center;
    font-size: 15px; font-weight: 300; color: var(--white);
  }
  .review__person {
    position: absolute; left: 0; right: 0; top: 51px;
    display: flex; gap: 10px; align-items: center; justify-content: center;
  }
  .review__avatar { width: 55px; height: 55px; border-radius: 50%; background: #4a3a36; flex: none; }
  .review__name { font-size: 12.5px; font-weight: 300; color: var(--white); }
  .review__stars { font-size: 11px; color: var(--gold); letter-spacing: 1px; }
  .copyright {
    position: absolute; left: 0; top: 1127px; width: 1200px; text-align: center;
    font-size: 12.5px; font-weight: 300; color: var(--white);
  }
</style>
</head>
<body>
  <header class="hero">
    <div class="hero__orb"></div>
    <div class="hero__visual" role="img" aria-label="Logistik-Collage: Frachtflugzeug, Containerschiff, Gabelstapler mit Paketen, Transporter und Lkw"></div>
    <div class="brand"><span class="brand__dot"></span><span class="brand__name">Velarix</span></div>
    <h1 class="hero__title">Expressversand /<br>Import von China<br>nach Deutschland</h1>
    <div class="hotline__label">24h Servicehotline</div>
    <div class="hotline__pill">
      <svg width="24" height="24" viewBox="0 0 24 24" fill="none" stroke="#fff" stroke-width="1.8" stroke-linejoin="round"><path d="M5 3l4 1 1 5-2 1.5a12 12 0 006 6L15.5 14l5 1 1 4-2 2C10 21 3 14 3 5z"/><path d="M14 3a7 7 0 017 7M14 6.5a3.5 3.5 0 013.5 3.5"/></svg>
      0987/314265
    </div>
  </header>

  <svg class="swirl" width="60" height="152" viewBox="0 0 60 152" fill="none" stroke="#c94e3a" stroke-width="4" stroke-linecap="round" stroke-linejoin="round">
    <path d="M56 4C24 2 6 30 12 62c5 24 40 28 42 10 2-16-26-14-34 4-12 28 4 58 32 70"/>
    <path d="M36 148l18-1-6-16"/>
  </svg>
  <p class="intro">Jetzt Angebot anfordern und günstig aus China per Express versenden.' Inkl. Abholung,<br>Verzollung und Zustellung. Kurze Laufzeit von nur 3-5 Tagen. ab 45€ / Paket</p>

  <form class="quote-form">
    <div class="quote-form__field">Firma</div>
    <div class="quote-form__field">Name</div>
    <div class="quote-form__field">Email Adresse</div>
    <div class="quote-form__field">Abholadresse in China</div>
    <div class="quote-form__field">Post Code</div>
    <div class="quote-form__field">ZielAdresse Deutschland</div>
    <div class="quote-form__field">Wie Viele Kartons</div>
    <div class="quote-form__field">Karton Gewicht</div>
    <div class="quote-form__field">Abmessungen&nbsp; L / W / H</div>
  </form>
  <div class="quote-form__send">
    <svg width="20" height="18" viewBox="0 0 20 18" fill="none" stroke="#fff" stroke-width="1.4" stroke-linejoin="round"><path d="M19 1L1 10l6 2 2 5 3-4 4 2z"/><path d="M7 12L19 1"/></svg>
    SENDEN
  </div>

  <section class="reviews"></section>
  <div class="reviews__mark">“</div>
  <h2 class="reviews__title">Was under Kunde sagt</h2>
  <div class="review-list">
    <div class="review">
      <p class="review__text">Schneller Versand - nur 4 Tage Laufzeit</p>
      <div class="review__person"><div class="review__avatar" role="img" aria-label="Porträtfoto eines Kunden"></div><div><div class="review__name">Marek Tonsel</div><div class="review__stars">★★★★★</div></div></div>
    </div>
    <div class="review">
      <p class="review__text">1A Service, ohne Probleme</p>
      <div class="review__person"><div class="review__avatar" role="img" aria-label="Porträtfoto eines Kunden"></div><div><div class="review__name">Jonas Pfeil</div><div class="review__stars">★★★★★</div></div></div>
    </div>
    <div class="review">
      <p class="review__text">Gute Preise - nur zu empfehlen.</p>
      <div class="review__person"><div class="review__avatar" role="img" aria-label="Porträtfoto eines Kunden"></div><div><div class="review__name">Marek Tonsel</div><div class="review__stars">★★★★★</div></div></div>
    </div>
  </div>
  <p class="copyright">Copyright 2021. Alle Rechte vorbehalten.</p>
</body>
</html>
```